Crisply Lantern Pocket Vegan Snack Bars Label

I am looking for a snack bar label design for my 3 Crisply Lantern Pocket Bars.

The flavors are:

Dulce de Leche
Mexican Hot Chocolate
Churro

I would like the name of the bar to be prominent and creative (different font for each) with presence of the logo. Clean, crisp, inviting and fun. I tend to like the white, tan/light brown and mint/aqua color scheme.

also, somewhere on the label it needs to say vegan, gluten free

I've attached my logo but POCKET needs to be added to it in a cool way as well.

The label dimensions are 4x31/3 and space needs to be left for nutrition table and ingredients

Thanks! (I have included my avatar as well for inspiration)

Target Market(s)

18-45, healthy eaters, young, hip, on the go, travel

Font styles to use
Decorative

Colors
87cfc6
ffffff
fbc994

Requirements
Must have
• the logo
Nice to have
• I like the idea of the name of the bars to look like the food it is ; )
Should not have
• too much stuff - no business

```html
<!DOCTYPE html>
<html lang="en">
<head>
<meta charset="utf-8">
<title>Crisply Lantern Pocket Bar – Churro Label</title>
<link rel="stylesheet" href="https://fonts.googleapis.com/css2?family=Fira+Sans+Condensed:ital,wght@1,900&family=Norican&family=Kalam:wght@700&family=Ubuntu:wght@400;700&display=swap">
<style>
  :root {
    --butter: #fede7e;
    --cocoa: #6b3319;
    --cocoa-deep: #5b2d14;
    --caramel: #e8951f;
    --tan-ghost: #ecb47c;
    --white: #ffffff;
    --crust: #e59a2c;
  }
  * { margin: 0; padding: 0; box-sizing: border-box; }
  html, body { width: 1200px; height: 1000px; overflow: hidden; }
  body { background: #d89a66; }
  .label {
    position: relative;
    width: 1200px;
    height: 1000px;
    overflow: hidden;
    background:
      radial-gradient(ellipse 140px 260px at 800px 830px, rgba(120,70,35,0.45), transparent 70%),
      linear-gradient(90deg, transparent 0, transparent 820px, rgba(245,215,165,0.75) 950px, rgba(230,195,150,0.6) 1020px, rgba(150,95,55,0.55) 1200px),
      linear-gradient(180deg, #b47a4c 0%, #c98a5a 30%, #de9a66 55%, #e39c66 100%);
  }
  .key-shape { position: absolute; left: 0; top: 0; }
  .brand-name {
    position: absolute;
    left: 107px; top: 355px;
    width: 200px;
    text-align: center;
    font-family: "Ubuntu", sans-serif;
    font-weight: 700;
    font-size: 27px;
    line-height: 1.1;
    color: var(--cocoa);
  }
  .product-line {
    position: absolute;
    left: 118px; top: 38px;
    font-family: "Fira Sans Condensed", sans-serif;
    font-style: italic;
    font-weight: 900;
    font-size: 282px;
    line-height: 1;
    letter-spacing: -4px;
    color: var(--butter);
  }
  .bar-word {
    position: absolute;
    left: 622px; top: 352px;
    font-family: "Fira Sans Condensed", sans-serif;
    font-style: italic;
    font-weight: 900;
    font-size: 108px;
    line-height: 1;
    color: var(--tan-ghost);
  }
  .claims {
    position: absolute;
    left: 350px; top: 380px;
    font-family: "Kalam", cursive;
    font-weight: 700;
    font-size: 30px;
    color: var(--white);
    word-spacing: 8px;
  }
  .flavor {
    position: absolute;
    left: 455px; top: 395px;
    font-family: "Norican", cursive;
    font-size: 190px;
    line-height: 1;
    color: var(--cocoa);
  }
  .flavor-art { position: absolute; left: 985px; top: 445px; }
  .band-dark { position: absolute; left: 0; top: 615px; width: 1200px; height: 26px; background: var(--cocoa); }
  .band-gold { position: absolute; left: 0; top: 641px; width: 1200px; height: 25px; background: var(--caramel); }
  .panel-info { position: absolute; left: 182px; top: 700px; width: 900px; }
  .info-heading {
    font-family: "Ubuntu", sans-serif;
    font-weight: 700;
    font-size: 22px;
    color: var(--cocoa-deep);
    line-height: 1;
  }
  .info-body {
    font-family: "Ubuntu", sans-serif;
    font-size: 22px;
    line-height: 32px;
    color: var(--cocoa);
    margin-top: 4px;
  }
  .info-block + .info-block { margin-top: 30px; }
  .info-block.ingredients .info-heading { margin-left: 4px; }
</style>
</head>
<body>
  <div class="label">
    <svg class="key-shape" width="1200" height="1000" viewBox="0 0 1200 1000" aria-hidden="true">
      <circle cx="207" cy="393" r="127" fill="var(--butter)"/>
      <rect x="207" y="328" width="500" height="132" fill="var(--butter)"/>
    </svg>

    <div class="product-line">POCKET</div>
    <div class="bar-word">BAR</div>

    <div class="brand-name">Crisply<br>Lantern</div>

    <div class="claims">·vegan ·gluten free</div>

    <div class="flavor">churro</div>
    <svg class="flavor-art" width="118" height="118" viewBox="0 0 118 118" role="img" aria-label="Illustration of a churro twisted into a heart shape">
      <path d="M59 112 C20 80 2 58 6 34 C10 12 36 4 52 22 L59 30 L66 22 C82 4 108 12 112 34 C116 58 98 80 59 112 Z" fill="var(--crust)"/>
    </svg>

    <div class="band-dark"></div>
    <div class="band-gold"></div>

    <div class="panel-info">
      <section class="info-block nutrition">
        <h2 class="info-heading">NUTRICION FACTS</h2>
        <p class="info-body">Lorem ipsum dolor sit amet enim. Etiam ullamcorper. Suspendisse a pellentesq<br>dui, non felis. Maecenas malesuada elit lectus felis,Curabitur et ligula. Ut mole<br>stie a, ultricies porta urna. Vestibulum commodo volutpat a, convallis ac, laore.</p>
      </section>
      <section class="info-block ingredients">
        <h2 class="info-heading">INGREDIENTS:</h2>
        <p class="info-body">Lorem ipsum dolor sit amet enim. Etiam ullamcorper. Suspendisse a pellentesq<br>dui, non felis. Maecenas malesuada elit lectus felis,Curabitur et ligula. Ut mole<br>stie a, ultricies porta urna. Vestibulum commodo volutpat a, convallis ac, laore.</p>
      </section>
    </div>
  </div>
</body>
</html>
```